Word Templates for Green Energy Consulting Company

Please see attached brief. This is what we'd like. Please note that we have also launched a PowerPoint template project and we want the two designs to be consistent. We encourage designers to submit to both contests. PowerPoint project is here: https://www.plintorava.com/manage-project/brief/5183620

Font styles to use
Serif
Sans Serif

```html
<!DOCTYPE html>
<html lang="en">
<head>
<meta charset="utf-8">
<title>Norvale Group – Report Templates</title>
<link rel="stylesheet" href="https://fonts.googleapis.com/css2?family=Arimo:ital,wght@0,400;0,700;1,400&family=Montserrat:wght@300;400;500;600;700&display=swap">
<style>
:root{
  --navy:#203348;
  --navy-deep:#1a2a44;
  --ink:#231F20;
  --green:#6DB044;
  --green-mid:#4C9944;
  --green-dark:#207A3D;
  --blue:#1687C3;
  --blue-deep:#1A567D;
  --title-blue:#1a6fa5;
  --bar:#1f4a6e;
  --bg:#c9cacc;
  --paper:#ffffff;
}
*{margin:0;padding:0;box-sizing:border-box}
html,body{width:1200px;height:3128px;overflow:hidden;background:var(--bg)}
body{position:relative;font-family:"Arimo",Arial,sans-serif;color:var(--ink)}
.page{position:absolute;width:400px;height:564px;background:var(--paper);overflow:hidden}
.page-shadow{position:absolute;width:400px;height:18px;background:linear-gradient(#8a8b8e,rgba(200,201,204,0))}
.col-a{left:178px}.col-b{left:633px}
.abs{position:absolute}
svg.abs{display:block}

/* photo placeholders */
.photo-sky{background:linear-gradient(180deg,#24395c 0%,#1d3354 60%,#1a2b47 100%)}
.photo-strip{background:linear-gradient(90deg,#1c2f4d,#2a4466 40%,#1f3657 70%,#1b2d4a)}

/* covers */
.back-title{left:0;width:400px;top:243px;text-align:center;font-family:"Montserrat",sans-serif;font-weight:600;font-size:27px;line-height:33px;color:var(--title-blue)}
.back-title .hl{color:var(--green)}
.brand-small{left:0;width:400px;top:413px;text-align:center;font-family:"Montserrat",sans-serif;font-weight:700;font-size:15px;color:var(--navy)}
.tag-small{left:130px;width:140px;top:433px;text-align:center;font-family:"Montserrat",sans-serif;font-size:6px;color:var(--green-mid);border-top:1px solid var(--green);padding-top:1px}
.contact{left:200px;width:200px;text-align:center;font-family:"Montserrat",sans-serif;font-size:8px;letter-spacing:.4px}
.title-box{left:100px;top:36px;width:199px;height:119px;border:3px solid var(--green);border-radius:10px;text-align:center;font-family:"Montserrat",sans-serif;color:#fff}
.title-box .t{font-size:38px;font-weight:500;line-height:44px;letter-spacing:1px}
.title-box .t:first-child{margin-top:3px}
.title-box .yr{position:absolute;left:42px;right:42px;bottom:-20px;background:var(--navy-deep);color:var(--green);font-weight:700;font-size:37px;line-height:40px}
.brand-large{left:0;width:400px;top:296px;text-align:center;font-family:"Montserrat",sans-serif;font-weight:700;font-size:29px;color:var(--navy)}
.tag-large{left:50px;width:300px;top:334px;text-align:center;font-family:"Montserrat",sans-serif;font-size:12px;color:var(--green-dark);display:flex;align-items:center;gap:8px;white-space:nowrap}
.tag-large::before,.tag-large::after{content:"";flex:1;height:1px;background:var(--green)}
.cover-url{left:0;width:400px;top:544px;text-align:center;font-family:"Montserrat",sans-serif;font-size:7px;letter-spacing:3.5px;color:#dfe8f0}

/* inner page chrome */
.head-band{left:0;top:0;width:400px;height:34px}
.head-rule{left:0;top:34px;width:400px;height:3px;background:var(--green-mid)}
.head-label{left:37px;top:13px;font-weight:700;font-size:12.5px;color:#fff;letter-spacing:.3px}
.foot-brand{left:18px;top:537px;font-family:"Montserrat",sans-serif;font-weight:700;font-size:9px;color:var(--navy);display:flex;align-items:center;gap:5px}
.foot-brand .mark{width:8px;height:8px;background:var(--green-mid)}
.foot-band{left:0;top:555px;width:400px;height:9px;background:linear-gradient(90deg,var(--blue),var(--navy))}

/* typography */
.h-green{font-weight:700;font-size:13px;color:var(--green-mid);letter-spacing:.2px}
.h-sub{font-size:8px;color:var(--blue-deep);margin-top:2px}
.h-sub.b{font-weight:700}
.body{font-family:"Montserrat",sans-serif;font-weight:400;font-size:5.6px;line-height:12.9px;color:#333;text-align:justify;margin-top:3px}
.body+.body{margin-top:12px}
.h-it{font-style:italic;font-size:8px;color:var(--blue-deep);margin-top:10px}

/* TOC */
.toc-title{left:36px;top:44px;font-weight:700;font-size:12px;line-height:14px;color:var(--navy)}
.toc-title .g{color:var(--green-mid)}
.toc{left:36px;top:95px;width:327px;list-style:none}
.toc li{display:flex;align-items:center;height:18px;margin-bottom:12.7px;font-size:7px;font-weight:700;color:#fff}
.toc .num{width:16px;height:16px;background:var(--green-mid);display:flex;align-items:center;justify-content:center}
.toc .label{flex:1;height:18px;margin:0 3px 0 6px;background:var(--bar);display:flex;align-items:center;padding-left:13px;letter-spacing:.2px}
.toc .pg{width:16px;height:16px;background:var(--green-mid);display:flex;align-items:center;justify-content:center}

/* style guide */
.spec1{font-weight:700;font-size:12px;color:var(--green-mid)}
.spec2{font-weight:700;font-size:8px;color:var(--navy);margin-top:3px}
.spec3{font-style:italic;font-size:8px;color:var(--blue-deep);margin-top:11px}
.spec4{font-family:"Montserrat",sans-serif;font-weight:300;font-size:6px;margin-top:5px}
.swatch{position:absolute;width:59px;height:48px;color:#fff;font-size:6px;display:flex;align-items:center;justify-content:center}
.cmyk{position:absolute;font-size:7.5px;line-height:11px;display:grid;grid-template-columns:24px 12px 20px;text-align:center}
.cmyk .g{color:var(--green)}
.cmyk .b{color:var(--blue)}
.cmyk .k{color:var(--navy)}
</style>
</head>
<body>

<!-- ROW 1 : covers -->
<section class="page col-a" style="top:77px" aria-label="Back cover">
  <div class="abs photo-sky" role="img" aria-label="Wind turbines at dusk" style="left:0;top:0;width:400px;height:200px;clip-path:polygon(0 0,100% 0,100% 94%,0 56%)"></div>
  <svg class="abs" style="left:0;top:0" width="400" height="564" viewBox="0 0 400 564">
    <polygon points="0,112 400,188 400,195 0,119" fill="#4C9944"/>
    <defs><linearGradient id="backWave" x1="0" x2="1"><stop offset="0" stop-color="#1687C3"/><stop offset="1" stop-color="#203348"/></linearGradient></defs>
    <path d="M0,492 H60 V526 Q200,440 400,458 V564 H0Z" fill="url(#backWave)"/>
  </svg>
  <h1 class="abs back-title">THE ENERGY<br>OF <span class="hl">CLEAR THINKING</span></h1>
  <div class="abs brand-small">Norvale Group</div>
  <div class="abs tag-small">The Energy of Clear Thinking</div>
  <div class="abs contact" style="top:509px;color:var(--green)">555-014-2291</div>
  <div class="abs contact" style="top:522px;color:#fff">info@norvalegroup.com</div>
  <div class="abs contact" style="top:534px;color:var(--green);font-size:10px;letter-spacing:1px">www.norvalegroup.com</div>
</section>
<div class="page-shadow col-a" style="top:641px"></div>

<section class="page col-b" style="top:77px" aria-label="Front cover">
  <div class="abs photo-sky" role="img" aria-label="Wind farm under an evening sky" style="left:0;top:0;width:400px;height:232px;clip-path:polygon(0 0,100% 0,100% 82%,50% 96%,0 82%)"></div>
  <svg class="abs" style="left:0;top:0" width="400" height="564" viewBox="0 0 400 564">
    <defs>
      <linearGradient id="spine" x1="0" x2="1"><stop offset="0" stop-color="#d6d7d9"/><stop offset="1" stop-color="#fff" stop-opacity="0"/></linearGradient>
      <linearGradient id="frontWave" x1="0" x2="1"><stop offset="0" stop-color="#203348"/><stop offset="1" stop-color="#1A567D"/></linearGradient>
    </defs>
    <polygon points="0,190 200,222 400,190 400,199 200,231 0,199" fill="#6DB044"/>
    <rect x="0" y="199" width="34" height="365" fill="url(#spine)"/>
    <path d="M0,512 Q240,560 365,470 L400,505 V564 H0Z" fill="url(#frontWave)"/>
    <path d="M260,368 H400 V505 L365,470 Q240,560 0,512 V498 Q230,525 328,432 Z" fill="#6DB044"/>
  </svg>
  <div class="abs title-box"><div class="t">ANNUAL</div><div class="t">REPORT</div><div class="yr">2023</div></div>
  <div class="abs brand-large">Norvale Group</div>
  <div class="abs tag-large">The Energy of Clear Thinking</div>
  <div class="abs cover-url">www.norvalegroup.com</div>
</section>
<div class="page-shadow col-b" style="top:641px"></div>

<!-- ROW 2 -->
<section class="page col-a" style="top:716px" aria-label="Table of contents">
  <div class="abs head-band photo-strip" role="img" aria-label="Wind turbine banner"></div>
  <div class="abs head-rule"></div>
  <h2 class="abs toc-title"><span class="g">TABLE</span><br>OF CONTENT</h2>
  <ol class="abs toc">
    <li><span class="num">1</span><span class="label">HEADING GOES HERE</span><span class="pg">01</span></li>
    <li><span class="num">2</span><span class="label">HEADING GOES HERE</span><span class="pg">02</span></li>
    <li><span class="num">3</span><span class="label">HEADING GOES HERE</span><span class="pg">03</span></li>
    <li><span class="num">4</span><span class="label">HEADING GOES HERE</span><span class="pg">04</span></li>
    <li><span class="num">5</span><span class="label">HEADING GOES HERE</span><span class="pg">05</span></li>
    <li><span class="num">6</span><span class="label">HEADING GOES HERE</span><span class="pg">06</span></li>
    <li><span class="num">7</span><span class="label">HEADING GOES HERE</span><span class="pg">07</span></li>
    <li><span class="num">8</span><span class="label">HEADING GOES HERE</span><span class="pg">08</span></li>
    <li><span class="num">9</span><span class="label">HEADING GOES HERE</span><span class="pg">09</span></li>
  </ol>
  <div class="abs foot-brand"><span class="mark"></span>Norvale Group</div>
  <svg class="abs" style="left:360px;top:530px" width="40" height="34" viewBox="0 0 40 34"><path d="M12,4 H40 V30 L33,23 Q20,34 0,30 V26 Q18,28 28,17 Z" fill="#4C9944"/></svg>
  <div class="abs foot-band"></div>
</section>
<div class="page-shadow col-a" style="top:1280px"></div>

<section class="page col-b" style="top:716px" aria-label="Text page with three sections">
  <div class="abs head-band photo-strip" role="img" aria-label="Wind turbine banner"></div>
  <div class="abs head-rule"></div>
  <div class="abs head-label">ENTER TEXT HERE</div>
  <div class="abs" style="left:37px;top:43px;width:322px">
    <h3 class="h-green">HEADING GOES HERE</h3><p class="h-sub">SUBTITLE GOES HERE</p>
    <p class="body">Lorem ipsum dolor sit amet, consectetuer adipiscing elit, sed diam nonummy nibh euismod tincidunt ut laoreet dolore magna aliquam erat volutpat. Ut wisi enim ad minim veniam, quis nostrud exerci tation ullamcorper suscipit lobortis nisl ut aliquip ex ea commodo consequat. Duis autem vel eum iriure dolor in hendrerit in vulputate velit esse molestie consequat, vel illum dolore eu feugiat nulla facilisis at vero eros et accumsan et iusto odio dignissim qui blandit praesent luptatum zzril delenit augue duis dolore te feugait nulla facilisi.</p>
    <p class="body">Lorem ipsum dolor sit amet, cons ectetuer adipiscing elit, sed diam nonummy nibh euismod tincidunt ut laoreet dolore magna aliquam erat volutpat. Ut wisi enim ad minim veniam, quis nostrud exerci tation ullamcorper suscipit lobortis nisl ut aliquip ex ea commodo consequat.</p>
    <h3 class="h-green" style="margin-top:16px">HEADING GOES HERE</h3><p class="h-sub">SUBTITLE GOES HERE</p>
    <p class="body" style="margin-top:0">Lorem ipsum dolor sit amet, consectetuer adipiscing elit, sed diam nonummy nibh euismod tincidunt ut laoreet dolore magna aliquam erat volutpat. Ut wisi enim ad minim veniam, quis nostrud exerci tation ullamcorper suscipit lobortis nisl ut aliquip ex ea commodo consequat. Duis autem vel eum iriure dolor in hendrerit in vulputate velit esse molestie consequat, vel illum dolore eu feugiat nulla facilisis at vero eros et accumsan et iusto odio dignissim qui blandit praesent luptatum zzril delenit augue duis dolore te feugait nulla facilisi.</p>
    <p class="body">Lorem ipsum dolor sit amet, cons ectetuer adipiscing elit, sed diam nonummy nibh euismod tincidunt ut laoreet dolore magna aliquam erat volutpat. Ut wisi enim ad minim veniam, quis nostrud exerci tation ullamcorper suscipit lobortis nisl ut aliquip ex ea commodo consequat.</p>
    <h3 class="h-green" style="margin-top:16px">HEADING GOES HERE</h3><p class="h-sub">SUBTITLE GOES HERE</p>
    <p class="body" style="margin-top:0">Lorem ipsum dolor sit amet, consectetuer adipiscing elit, sed diam nonummy nibh euismod tincidunt ut laoreet dolore magna aliquam erat volutpat. Ut wisi enim ad minim veniam, quis nostrud exerci tation ullamcorper suscipit lobortis nisl ut aliquip ex ea commodo consequat. Duis autem vel eum iriure dolor in hendrerit in vulputate velit esse molestie consequat, vel illum dolore eu feugiat nulla facilisis at vero eros et accumsan et iusto odio dignissim qui blandit praesent luptatum zzril delenit augue duis dolore te feugait nulla facilisi.</p>
    <p class="body">Lorem ipsum dolor sit amet, cons ectetuer adipiscing elit, sed diam nonummy nibh euismod tincidunt ut laoreet dolore magna aliquam erat volutpat. Ut wisi enim ad minim veniam, quis nostrud exerci tation ullamcorper suscipit lobortis nisl ut aliquip ex ea commodo consequat.</p>
  </div>
  <div class="abs foot-brand"><span class="mark"></span>Norvale Group</div>
  <svg class="abs" style="left:360px;top:530px" width="40" height="34" viewBox="0 0 40 34"><path d="M12,4 H40 V30 L33,23 Q20,34 0,30 V26 Q18,28 28,17 Z" fill="#4C9944"/></svg>
  <div class="abs foot-band"></div>
</section>
<div class="page-shadow col-b" style="top:1280px"></div>

<!-- ROW 3 -->
<section class="page col-a" style="top:1333px" aria-label="Text page with image">
  <div class="abs head-band photo-strip" role="img" aria-label="Wind turbine banner"></div>
  <div class="abs head-rule"></div>
  <div class="abs head-label">ENTER TEXT HERE</div>
  <div class="abs" style="left:37px;top:43px;width:326px">
    <h3 class="h-green">HEADING GOES HERE</h3><p class="h-sub">SUBTITLE GOES HERE</p>
    <p class="body">Lorem ipsum dolor sit amet, consectetuer adipiscing elit, sed diam nonummy nibh euismod tincidunt ut laoreet dolore magna aliquam erat volutpat. Ut wisi enim ad minim veniam, quis nostrud exerci tation ullamcorper suscipit lobortis nisl ut aliquip ex ea commodo consequat. Duis autem vel eum iriure dolor in hendrerit in vulputate velit esse molestie consequat, vel illum dolore eu feugiat nulla facilisis at vero eros et accumsan et iusto odio dignissim qui blandit praesent luptatum zzril delenit augue duis dolore te feugait nulla facilisi.</p>
    <p class="body">Lorem ipsum dolor sit amet, cons ectetuer adipiscing elit, sed diam nonummy nibh euismod tincidunt ut laoreet dolore magna aliquam erat volutpat. Ut wisi enim ad minim veniam, quis nostrud exerci tation ullamcorper suscipit lobortis nisl ut aliquip ex ea commodo consequat.</p>
    <p class="body">Lorem ipsum dolor sit amet, consectetuer adipiscing elit, sed diam nonummy nibh euismod tincidunt ut laoreet dolore magna aliquam erat volutpat. Ut wisi enim ad minim veniam, quis nostrud exerci tation ullamcorper suscipit lobortis nisl ut aliquip ex ea commodo consequat. Duis autem vel eum iriure dolor in hendrerit in vulputate velit esse molestie consequat, vel illum dolore eu feugiat nulla facilisis at vero eros et accumsan et iusto odio dignissim qui blandit praesent luptatum zzril delenit augue duis dolore te feugait nulla facilisi.</p>
  </div>
  <div class="abs" style="left:37px;top:283px;width:326px">
    <h3 class="h-green">HEADING GOES HERE</h3><p class="h-sub">SUBTITLE GOES HERE</p>
  </div>
  <p class="abs body" style="left:37px;top:318px;width:163px">Lorem ipsum dolor sit amet, consectetuer adipiscing elit, sed diam nonummy nibh euismod tincidunt ut laoreet dolore magna aliquam erat volutpat. Ut wisi enim ad minim veniam, quis nostrud exerci tation ullamcorper suscipit lobortis nisl ut aliquip ex ea commodo consequat. Duis autem vel eum iriure dolor in hendrerit in vulputate velit esse molestie consequat, vel illum dolore eu feugiat nulla facilisis at vero eros et accumsan et iusto odio dignissim qui blandit praesent luptatum zzril delenit augue duis dolore te feugait nulla facilisi. vulputate velit esse molestie consequat, vel illum dolore eu feugiat nulla facilisis at vero eros et accumsan et iusto odio dignissim qui blandit praesent luptatum zzril delenit augue duis dolore te feugait nulla facilisi.</p>
  <div class="abs" role="img" aria-label="Hands raising light bulbs against a bright sky" style="left:210px;top:323px;width:153px;height:174px;background:linear-gradient(180deg,#dfe9f2 0%,#c9d8e4 45%,#8fa57e 80%,#6f8a62 100%)"></div>
  <div class="abs foot-brand"><span class="mark"></span>Norvale Group</div>
  <svg class="abs" style="left:360px;top:530px" width="40" height="34" viewBox="0 0 40 34"><path d="M12,4 H40 V30 L33,23 Q20,34 0,30 V26 Q18,28 28,17 Z" fill="#4C9944"/></svg>
  <div class="abs foot-band"></div>
</section>
<div class="page-shadow col-a" style="top:1897px"></div>

<section class="page col-b" style="top:1333px" aria-label="Text page with numbered headings">
  <div class="abs head-band photo-strip" role="img" aria-label="Wind turbine banner"></div>
  <div class="abs head-rule"></div>
  <div class="abs head-label">ENTER TEXT HERE</div>
  <div class="abs" style="left:37px;top:43px;width:324px">
    <h3 class="h-green">HEADING GOES HERE</h3><p class="h-sub b">SUBTITLE GOES HERE</p>
    <p class="h-it">"1." Heading 1</p>
    <p class="body" style="margin-top:0">Lorem ipsum dolor sit amet, consectetuer adipiscing elit, sed diam nonummy nibh euismod tincidunt ut laoreet dolore magna aliquam erat volutpat. Ut wisi enim ad minim veniam, quis nostrud exerci tation ullamcorper suscipit lobortis nisl ut aliquip ex ea commodo consequat. Duis autem vel eum iriure dolor in hendrerit in vulputate velit esse molestie consequat, vel illum dolore eu feugiat nulla facilisis at vero eros et accumsan et iusto odio dignissim qui blandit praesent luptatum zzril delenit augue duis dolore te feugait nulla facilisi.</p>
    <p class="h-it">"1.1. Heading 2</p>
    <p class="body" style="margin-top:0">Lorem ipsum dolor sit amet, consectetuer adipiscing elit, sed diam nonummy nibh euismod tincidunt ut laoreet dolore magna aliquam erat volutpat. Ut wisi enim ad minim veniam, quis nostrud exerci tation ullamcorper suscipit lobortis nisl ut aliquip ex ea commodo consequat. Duis autem vel eum iriure dolor in hendrerit in vulputate velit esse molestie consequat, vel illum dolore eu feugiat nulla facilisis at vero eros et accumsan et iusto odio dignissim qui blandit praesent luptatum zzril delenit augue duis dolore te feugait nulla facilisi.</p>
    <p class="h-it">"1.1.1. Heading 3</p>
    <p class="body" style="margin-top:0">Lorem ipsum dolor sit amet, consectetuer adipiscing elit, sed diam nonummy nibh euismod tincidunt ut laoreet dolore magna aliquam erat volutpat. Ut wisi enim ad minim veniam, quis nostrud exerci tation ullamcorper suscipit lobortis nisl ut aliquip ex ea commodo consequat. Duis autem vel eum iriure dolor in hendrerit in vulputate velit esse molestie consequat, vel illum dolore eu feugiat nulla facilisis at vero eros et accumsan et iusto odio dignissim qui blandit praesent luptatum zzril delenit augue duis dolore te feugait nulla facilisi.</p>
  </div>
  <div class="abs foot-brand"><span class="mark"></span>Norvale Group</div>
  <svg class="abs" style="left:360px;top:530px" width="40" height="34" viewBox="0 0 40 34"><path d="M12,4 H40 V30 L33,23 Q20,34 0,30 V26 Q18,28 28,17 Z" fill="#4C9944"/></svg>
  <div class="abs foot-band"></div>
</section>
<div class="page-shadow col-b" style="top:1897px"></div>

<!-- ROW 4 -->
<section class="page col-a" style="top:1955px" aria-label="Two column text page">
  <div class="abs head-band photo-strip" role="img" aria-label="Wind turbine banner"></div>
  <div class="abs head-rule"></div>
  <div class="abs head-label">ENTER TEXT HERE</div>
  <div class="abs" style="left:38px;top:69px;width:151px">
    <h3 class="h-green">HEADING GOES HERE</h3><p class="h-sub">SUBTITLE GOES HERE</p>
    <p class="body" style="margin-top:6px">Lorem ipsum dolor sit amet, consectetuer adipiscing elit, sed diam nonummy nibh euismod tincidunt ut laoreet dolore magna aliquam erat volutpat. Ut wisi enim ad minim veniam, quis nostrud exerci tation ullamcorper suscipit lobortis nisl ut aliquip ex ea commodo consequat. Duis autem vel eum iriure dolor in hendrerit in vulputate velit esse molestie consequat, vel illum dolore eu feugiat nulla facilisis at vero eros et accumsan et iusto odio dignissim qui blandit praesent luptatum zzril delenit augue duis dolore te feugait nulla facilisi. vulputate velit esse molestie consequat, vel illum dolore eu feugiat nulla facilisis at vero eros et accumsan et iusto odio dignissim qui blandit praesent luptatum zzril delenit augue duis dolore te feugait nulla facilisi. vulputate velit esse molestie consequat, vel illum dolore eu feugiat nulla facilisis at vero eros et accumsan et iusto odio dignissim qui blandit praesent luptatum zzril delenit augue duis dolore te feugait nulla facilisi. vulputate velit esse molestie consequat, vel illum dolore eu feugiat nulla facilisis at vero eros et accumsan et iusto odio dignissim qui blandit praesent luptatum zzril delenit augue duis dolore te feugait nulla facilisi.</p>
  </div>
  <div class="abs" style="left:212px;top:69px;width:151px">
    <h3 class="h-green">HEADING GOES HERE</h3><p class="h-sub">SUBTITLE GOES HERE</p>
    <p class="body" style="margin-top:6px">Lorem ipsum dolor sit amet, consectetuer adipiscing elit, sed diam nonummy nibh euismod tincidunt ut laoreet dolore magna aliquam erat volutpat. Ut wisi enim ad minim veniam, quis nostrud exerci tation ullamcorper suscipit lobortis nisl ut aliquip ex ea commodo consequat. Duis autem vel eum iriure dolor in hendrerit in vulputate velit esse molestie consequat, vel illum dolore eu feugiat nulla facilisis at vero eros et accumsan et iusto odio dignissim qui blandit praesent luptatum zzril delenit augue duis dolore te feugait nulla facilisi. vulputate velit esse molestie consequat, vel illum dolore eu feugiat nulla facilisis at vero eros et accumsan et iusto odio dignissim qui blandit praesent luptatum zzril delenit augue duis dolore te feugait nulla facilisi. vulputate velit esse molestie consequat, vel illum dolore eu feugiat nulla facilisis at vero eros et accumsan et iusto odio dignissim qui blandit praesent luptatum zzril delenit augue duis dolore te feugait nulla facilisi. vulputate velit esse molestie consequat, vel illum dolore eu feugiat nulla facilisis at vero eros et accumsan et iusto odio dignissim qui blandit praesent luptatum zzril delenit augue duis dolore te feugait nulla facilisi.</p>
  </div>
  <div class="abs foot-brand"><span class="mark"></span>Norvale Group</div>
  <svg class="abs" style="left:360px;top:530px" width="40" height="34" viewBox="0 0 40 34"><path d="M12,4 H40 V30 L33,23 Q20,34 0,30 V26 Q18,28 28,17 Z" fill="#4C9944"/></svg>
  <div class="abs foot-band"></div>
</section>
<div class="page-shadow col-a" style="top:2519px"></div>

<section class="page col-b" style="top:1955px" aria-label="Type and colour guide">
  <div class="abs head-band photo-strip" role="img" aria-label="Wind turbine banner"></div>
  <div class="abs head-rule"></div>
  <div class="abs head-label">ENTER TEXT HERE</div>
  <div class="abs" style="left:36px;top:44px">
    <p class="spec1">HELVITICA BOLD 18</p>
    <p class="spec2">HELVITICA BOLD 12</p>
    <p class="spec3">Helvitica Oblique 12</p>
    <p class="spec4">Montserrat Light 9</p>
  </div>
  <div class="swatch" style="left:37px;top:123px;background:linear-gradient(90deg,#2a8a3c,#6DB044)"></div>
  <div class="cmyk" style="left:104px;top:126px"><span class="g">63</span><span class="k">C</span><span class="k">85</span><span class="g">8</span><span class="k">M</span><span class="k">27</span><span class="g">100</span><span class="k">Y</span><span class="k">100</span><span class="g">0.34</span><span class="k">K</span><span class="k">17</span></div>
  <div class="swatch" style="left:177px;top:123px;background:var(--green-dark)">#207A3D</div>
  <div class="swatch" style="left:263px;top:123px;background:var(--green)">#6DB044</div>
  <div class="swatch" style="left:37px;top:185px;background:linear-gradient(90deg,#1687C3,#203348)"></div>
  <div class="cmyk" style="left:104px;top:188px"><span class="b">81</span><span class="k">C</span><span class="k">90</span><span class="b">36</span><span class="k">M</span><span class="k">75</span><span class="b">3.5</span><span class="k">Y</span><span class="k">47</span><span class="b">0</span><span class="k">K</span><span class="k">44</span></div>
  <div class="swatch" style="left:177px;top:185px;background:var(--navy)">#203348</div>
  <div class="swatch" style="left:263px;top:185px;background:var(--blue)">#1687C3</div>
  <div class="swatch" style="left:37px;top:256px;background:var(--green-mid)">#4C9944</div>
  <div class="swatch" style="left:37px;top:317px;background:var(--blue-deep)">#1A567D</div>
  <div class="swatch" style="left:37px;top:379px;background:var(--ink)">#231F20</div>
  <div class="abs foot-brand"><span class="mark"></span>Norvale Group</div>
  <svg class="abs" style="left:360px;top:530px" width="40" height="34" viewBox="0 0 40 34"><path d="M12,4 H40 V30 L33,23 Q20,34 0,30 V26 Q18,28 28,17 Z" fill="#4C9944"/></svg>
  <div class="abs foot-band"></div>
</section>
<div class="page-shadow col-b" style="top:2519px"></div>

</body>
</html>
```